Real Estate Company Needs a Just Sold Flyer for 2 Residential Income Properties

We need a fresh, modern and contemporary "Just Sold" postcard for 2 Residential Income Properties located in South Pasadena, California. We would like to feature two buildings on a 2 sided -postcard. The two buildings can be located on the front of the postcard or one building can be featured in front and the other can be featured on the back.

The dimensions of the post cards are

Oversized

(8.52" x 5.47")

Target Market(s)

Residential Homeowners

Industry/Entity Type

Building

Colors
faee3f

Requirements
Must have
• The postcard must have 2 sides and use all the photos we have attached. Designer can be creative and place 2 buildings in front of the post card or a building on each side. "Just Sold" must be listed on the Front of the Post Card. Company Logo must be featured on each side. On the Back of the Post card should list the following names.

Leonard T. Brisbee
Broker
Brisbee Commercial Real Estate Services
5172 N Larkfield Ave, Suite 218
West Hollywood, Ca. 90412
www.brisbeecommercial.example
877-555-0193.

Also, on the back of the Post Card, we would like an empty space or block to add a paragraph about the two Property (Description will be provided)

Each building has three additional photographs for each property.
Nice to have
• Logo should be located at the same location on each side of the post card . The contact information should be placed on the 2nd Page of the Postcard.

Also, bullet points featuring the Properties can be placed on the Front of the Post Card (Description will be provided).

Please see the 2708 Thornby Lane Flyer that we picked a few weeks ago for a theme we are looking for. We like it fresh, contemporary and nice fonts.
Should not have
• No default fonts such as Arial or Times New Roman.

```html
<!DOCTYPE html>
<html lang="en">
<head>
<meta charset="utf-8">
<title>Brisbee Commercial – Just Sold Postcard</title>
<link href="https://fonts.googleapis.com/css2?family=Open+Sans:wght@400;700&family=Montserrat:wght@500&family=Great+Vibes&display=swap" rel="stylesheet">
<style>
  :root {
    --backdrop: #2a2a2a;
    --paper: #ffffff;
    --yellow: #faee3f;
    --yellow-deep: #f3cf1c;
    --ink: #2b2b2b;
    --blue: #2a4d9c;
    --script-blue: #2f5d9e;
    --frame: #4a4a4a;
    --silver: #bfc1c4;
  }
  html, body {
    margin: 0; padding: 0;
    width: 1200px; height: 1200px;
    overflow: hidden;
    background: var(--backdrop);
  }
  .card {
    position: absolute;
    left: 170px;
    width: 636px; height: 408px;
    background: var(--paper);
    transform-origin: 0 0;
    transform: scale(1.352);
    overflow: hidden;
    font-family: "Open Sans", sans-serif;
  }
  .card--back { top: 30px; }
  .card--front { top: 618px; }
  .card svg.shapes { position: absolute; inset: 0; }

  .brand {
    position: absolute;
    text-align: center;
    font-family: "Montserrat", sans-serif;
    font-weight: 500;
    color: var(--ink);
    text-transform: uppercase;
    line-height: 1.35;
  }
  .brand--back { left: 430px; top: 52px; width: 86px; font-size: 8.5px; letter-spacing: 1.6px; }
  .brand--front { left: 18px; top: 318px; width: 150px; font-size: 13px; letter-spacing: 3px; }

  .agent {
    position: absolute;
    left: 8px; top: 300px; width: 164px;
    text-align: center;
    color: var(--blue);
  }
  .agent__name { font-weight: 700; font-size: 13.5px; line-height: 1.2; }
  .agent__title { font-size: 10.5px; }

  .contact {
    position: absolute;
    left: 180px; top: 281px;
    font-size: 10px;
    line-height: 12.6px;
    color: var(--ink);
  }
  .contact__row { display: flex; align-items: flex-start; gap: 4px; }
  .contact__row svg { flex: none; margin-top: 2px; }
  .contact__gap { height: 5px; }

  .just-sold {
    position: absolute;
    left: 305px; top: 292px;
    font-family: "Great Vibes", cursive;
    font-size: 70px;
    color: var(--script-blue);
    white-space: nowrap;
  }
</style>
</head>
<body>

<!-- Back of postcard -->
<section class="card card--back">
  <svg class="shapes" viewBox="0 0 636 408" width="636" height="408">
    <defs>
      <linearGradient id="photoGarden" x1="0" y1="0" x2="0" y2="1">
        <stop offset="0" stop-color="#b9c4c6"/>
        <stop offset="0.55" stop-color="#c9bca2"/>
        <stop offset="1" stop-color="#6f8a4e"/>
      </linearGradient>
      <linearGradient id="photoInterior" x1="0" y1="0" x2="1" y2="1">
        <stop offset="0" stop-color="#d9d3c6"/>
        <stop offset="1" stop-color="#8a6c4f"/>
      </linearGradient>
      <linearGradient id="bandYellow" x1="0" y1="0" x2="1" y2="0">
        <stop offset="0" stop-color="var(--yellow-deep)"/>
        <stop offset="0.6" stop-color="var(--yellow)"/>
        <stop offset="1" stop-color="#f8e23a"/>
      </linearGradient>
      <linearGradient id="bandSilver" x1="0" y1="0" x2="1" y2="0">
        <stop offset="0" stop-color="#f2f2f2"/>
        <stop offset="0.5" stop-color="#b7b9bc"/>
        <stop offset="1" stop-color="#6d6f72"/>
      </linearGradient>
    </defs>

    <rect class="photo" role="img" aria-label="Property exterior with garden path" x="7" y="12" width="128" height="96" rx="10" fill="url(#photoGarden)" stroke="var(--frame)" stroke-width="1"/>
    <rect class="photo" role="img" aria-label="Property kitchen" x="139" y="12" width="89" height="46" rx="8" fill="url(#photoInterior)" stroke="var(--frame)" stroke-width="1"/>
    <rect class="photo" role="img" aria-label="Property living room with fireplace" x="139" y="62" width="89" height="46" rx="8" fill="url(#photoInterior)" stroke="var(--frame)" stroke-width="1"/>
    <rect class="description-box" x="235" y="12" width="188" height="96" rx="10" fill="#fff" stroke="var(--frame)" stroke-width="1"/>

    <rect class="photo" role="img" aria-label="Second property courtyard entrance" x="7" y="123" width="128" height="96" rx="10" fill="url(#photoGarden)" stroke="var(--frame)" stroke-width="1"/>
    <rect class="photo" role="img" aria-label="Second property living room" x="139" y="123" width="89" height="46" rx="8" fill="url(#photoInterior)" stroke="var(--frame)" stroke-width="1"/>
    <rect class="photo" role="img" aria-label="Second property sitting room" x="139" y="173" width="89" height="46" rx="8" fill="url(#photoInterior)" stroke="var(--frame)" stroke-width="1"/>
    <rect class="description-box" x="235" y="123" width="188" height="96" rx="10" fill="#fff" stroke="var(--frame)" stroke-width="1"/>

    <circle class="brand-dot" cx="473" cy="32" r="13" fill="var(--yellow)"/>
    <rect class="stamp-box" x="535" y="5" width="93" height="93" fill="none" stroke="#9a9a9a" stroke-width="1"/>

    <path d="M0,250 C140,262 300,252 423,222 L423,236 C300,262 140,276 0,268 Z" fill="url(#bandSilver)"/>
    <path d="M0,262 C150,274 300,258 423,228" fill="none" stroke="#2e2e2e" stroke-width="2.4"/>
    <path d="M0,264 C150,276 300,260 423,230 L423,354 L0,354 Z" fill="url(#bandYellow)"/>
    <line x1="0" y1="355" x2="423" y2="355" stroke="#333" stroke-width="1.5"/>
    <line x1="175" y1="280" x2="175" y2="350" stroke="var(--blue)" stroke-width="0.8"/>
  </svg>

  <div class="brand brand--back">Brisbee<br>Commercial</div>

  <div class="agent">
    <div class="agent__name">Leonard T. Brisbee</div>
    <div class="agent__title">Broker</div>
  </div>

  <div class="contact">
    <div class="contact__row">
      <svg width="7" height="9" viewBox="0 0 10 13"><path d="M5,0 C2.2,0 0,2.2 0,5 C0,8.5 5,13 5,13 C5,13 10,8.5 10,5 C10,2.2 7.8,0 5,0 Z M5,7 A2,2 0 1,1 5,3 A2,2 0 1,1 5,7 Z" fill="var(--blue)"/></svg>
      <div><span style="color:var(--blue)">Brisbee Commercial Real Estate Services</span><br>5172 N Larkfield Ave, Suite 218<br>West Hollywood, Ca. 90412</div>
    </div>
    <div class="contact__gap"></div>
    <div class="contact__row">
      <svg width="8" height="8" viewBox="0 0 10 10"><circle cx="5" cy="5" r="4.3" fill="none" stroke="var(--blue)" stroke-width="1.2"/><path d="M0.7,5 H9.3 M5,0.7 C2.5,3 2.5,7 5,9.3 M5,0.7 C7.5,3 7.5,7 5,9.3" fill="none" stroke="var(--blue)" stroke-width="0.9"/></svg>
      <div>www.brisbeecommercial.example</div>
    </div>
    <div class="contact__row">
      <svg width="8" height="8" viewBox="0 0 10 10"><path d="M2,0.5 L3.8,0.5 L4.5,3 L3.2,4 C3.8,5.4 4.6,6.2 6,6.8 L7,5.5 L9.5,6.2 L9.5,8 C9.5,9 8.5,9.6 7.5,9.4 C4,8.6 1.4,6 0.6,2.5 C0.4,1.5 1,0.5 2,0.5 Z" fill="var(--blue)"/></svg>
      <div>877-555-0193</div>
    </div>
  </div>
</section>

<!-- Front of postcard -->
<section class="card card--front">
  <svg class="shapes" viewBox="0 0 636 408" width="636" height="408">
    <defs>
      <linearGradient id="photoHouseA" x1="0" y1="0" x2="0" y2="1">
        <stop offset="0" stop-color="#7fa3cf"/>
        <stop offset="0.45" stop-color="#e2d6b4"/>
        <stop offset="0.75" stop-color="#5f8a3c"/>
        <stop offset="1" stop-color="#d8d2c2"/>
      </linearGradient>
      <linearGradient id="photoHouseB" x1="0" y1="0" x2="0" y2="1">
        <stop offset="0" stop-color="#c8cfd4"/>
        <stop offset="0.45" stop-color="#a79d91"/>
        <stop offset="0.7" stop-color="#4f7a35"/>
        <stop offset="1" stop-color="#6f9a3c"/>
      </linearGradient>
      <linearGradient id="sweepSilver" x1="0" y1="0" x2="1" y2="0">
        <stop offset="0" stop-color="#ffffff"/>
        <stop offset="0.55" stop-color="#e9eaeb"/>
        <stop offset="1" stop-color="#9fa2a5"/>
      </linearGradient>
      <linearGradient id="sweepYellow" x1="0" y1="0" x2="1" y2="0">
        <stop offset="0" stop-color="var(--yellow-deep)"/>
        <stop offset="0.5" stop-color="var(--yellow)"/>
        <stop offset="1" stop-color="var(--yellow-deep)"/>
      </linearGradient>
    </defs>

    <rect class="photo" role="img" aria-label="First sold property: cream stucco house with terraced lawn" x="0" y="0" width="317" height="255" fill="url(#photoHouseA)"/>
    <rect class="photo" role="img" aria-label="Second sold property: gabled house behind garden and lawn" x="319" y="0" width="317" height="255" fill="url(#photoHouseB)"/>

    <path d="M0,182 C180,232 420,250 636,186 L636,408 L0,408 Z" fill="url(#sweepSilver)"/>
    <path d="M0,182 C180,232 420,250 636,186" fill="none" stroke="#2e2e2e" stroke-width="3"/>
    <path d="M0,196 C180,246 420,262 636,200" fill="none" stroke="var(--silver)" stroke-width="6" opacity="0.7"/>
    <path d="M0,372 C220,382 450,340 636,262 L636,300 C450,370 220,392 0,388 Z" fill="#b4b6b9"/>
    <path d="M0,384 C220,394 450,352 636,274" fill="none" stroke="#2e2e2e" stroke-width="3"/>
    <path d="M0,388 C220,398 450,356 636,278 L636,408 L0,408 Z" fill="url(#sweepYellow)"/>

    <circle class="brand-dot" cx="93" cy="270" r="24" fill="var(--yellow)"/>
  </svg>

  <div class="brand brand--front">Brisbee<br>Commercial</div>

  <div class="just-sold">Just Sold</div>
</section>

</body>
</html>
```